Update existing website to a one page design.

Combine a multi page website into a single page design.
Existing site is at ac.calmharborcover (dot) com.
Rearrange elements as needed to create a modem look.
Not every element / all of the text need to be kept, design should be flexible enough to allow for new text (of different length) to be used.
Site should have a clear calls to action, such as get a quote and contact us.
Ability, call to action, to switch to Russian should be clearly visible near the top, translation will not be done by google, thus attribution is not needed.
Unused features (such as blog) should be dropped.
Images, besides logos, can be brand new.
Site should adhere to standard design practices (such as grid) and ideally be compatible with existing framework (such as bootstrap).
Coding of the website will likely be done by the winning bidder as a separate project.

```html
<!DOCTYPE html>
<html lang="en">
<head>
<meta charset="utf-8">
<title>Calm Harbor Cover</title>
<link rel="stylesheet" href="https://fonts.googleapis.com/css2?family=Arvo:wght@700&family=Montserrat:wght@400;500;600;700&display=swap">
<style>
:root{
  --navy:#060d29;
  --white:#ffffff;
  --ink:#0b1330;
  --body-grey:#555a66;
  --rule:#1a2346;
  --brand-blue:#1450a8;
  --gold:#c8b267;
  --gold-deep:#a89450;
  --accent:#d9a441;
}
*{box-sizing:border-box;margin:0;padding:0}
html,body{width:1200px;height:2247px;overflow:hidden}
body{position:relative;background:var(--navy);color:var(--white);font-family:'Montserrat',sans-serif}
.abs{position:absolute}
.heading{font-family:'Arvo',serif;font-weight:700}

/* header */
.hero{left:0;top:0;width:1200px;height:1017px;background:var(--navy)}
.brand-mark{left:99px;top:38px;width:128px;height:127px;background:var(--brand-blue);display:flex;align-items:flex-end;justify-content:center;padding-bottom:14px}
.brand-mark span{font-family:'Montserrat',sans-serif;font-weight:700;font-size:17px;color:var(--white);text-align:center;line-height:1.1}
.site-title{left:290px;top:32px;width:680px;text-align:center;font-size:43px;letter-spacing:.5px}
.lang-switch{left:1068px;top:44px;display:flex;border:1px solid var(--accent);border-radius:4px;overflow:hidden;font-size:14px;font-weight:600}
.lang-switch a{display:block;padding:7px 14px;color:var(--white);text-decoration:none}
.lang-switch a.current{background:var(--accent);color:var(--navy)}
.main-nav{left:0;top:198px;width:1200px;font-size:16px;font-weight:500}
.main-nav a{position:absolute;color:var(--white);text-decoration:none;white-space:nowrap}

/* carousel */
.slide{left:29px;top:252px;width:745px;height:264px;background:linear-gradient(100deg,#7c8aa0 0%,#b89a7a 35%,#4d5a3a 70%,#2f3a26 100%)}
.slide-arrow{top:378px;width:42px;height:42px;display:flex;align-items:center;justify-content:center}
.slide-arrow.prev{left:38px;background:rgba(40,70,80,.75)}
.slide-arrow.next{left:721px}
.dots{left:384px;top:526px;display:flex;gap:8px;align-items:center}
.dot{width:10px;height:10px;border-radius:50%;background:#8a8f9e}
.dot.active{width:13px;height:13px;background:var(--white)}
.gallery{left:806px;top:252px;width:372px;display:grid;grid-template-columns:repeat(3,122px);grid-auto-rows:122px;gap:3px}
.gallery div:nth-child(3n+1){background:linear-gradient(135deg,#e9ecef,#b99a6c)}
.gallery div:nth-child(3n+2){background:linear-gradient(180deg,#eef1ee,#5a5d58)}
.gallery div:nth-child(3n){background:linear-gradient(180deg,#2c6fc0,#e6e4dc 60%,#2d9a8e)}

/* quote CTA */
.cta-link{left:29px;top:582px;font-size:15px;color:var(--white);text-decoration:underline;letter-spacing:.2px}
.cta-title{left:29px;top:632px;font-size:24px;letter-spacing:.3px}
.cta-text{left:29px;top:693px;width:800px;font-size:16px;line-height:29px}

/* stats */
.stats{left:153px;top:806px;display:flex;gap:32px}
.stat{width:155px;height:153px;border-top:1px solid var(--rule);border-bottom:1px solid var(--rule);text-align:center;padding-top:33px}
.stat-label{font-size:16px;font-weight:600}
.stat-value{font-size:48px;font-weight:700;margin-top:8px;line-height:1.2}

/* about */
.about{left:0;top:1017px;width:1200px;height:372px;background:var(--white);color:var(--ink)}
.about-title{left:44px;top:28px;font-size:32px;color:var(--ink)}
.about-photo{left:87px;top:92px;width:274px;height:163px;background:linear-gradient(90deg,#7aa36a,#e8c38a 45%,#d6a040)}
.about-text{left:438px;top:32px;width:724px;font-size:16.5px;line-height:28.7px;color:var(--body-grey)}
.about-text p+p{margin-top:28px}
.about-text strong{color:var(--ink);font-weight:600}

/* banner */
.banner{left:0;top:1389px;width:1200px;height:589px;background:linear-gradient(100deg,#c9b677 0%,var(--gold) 45%,var(--gold-deep) 100%)}
.banner-title{left:290px;top:128px;width:620px;text-align:center;font-size:49px;line-height:55px;color:var(--ink)}
.banner-text{left:270px;top:480px;width:660px;text-align:center;font-size:15px;line-height:28.7px;color:#3a3a3a}

/* footer */
.footer{left:0;top:1978px;width:1200px;height:269px;background:var(--navy)}
.agent-photo{left:154px;top:37px;width:54px;height:82px;background:linear-gradient(180deg,#5f8a8c,#1d2c3e)}
.footer-title{top:38px;font-size:24px}
.footer-text{top:92px;font-size:15.5px;line-height:28.7px}
.footer-text .accent{color:var(--accent)}
</style>
</head>
<body>

<section class="hero abs">
  <div class="brand-mark abs"><span>CALM<br>HARBOR</span></div>
  <h1 class="site-title abs heading">CALM HARBOR COVER</h1>
  <nav class="lang-switch abs" aria-label="Language">
    <a class="current" lang="en">EN</a>
    <a lang="ru">RU</a>
  </nav>
  <nav class="main-nav abs">
    <a style="left:144px">Individual health</a>
    <a style="left:379px">Group Health</a>
    <a style="left:586px">Doctors Network</a>
    <a style="left:822px">Get an Instant Quote</a>
    <a style="left:1090px">Contact Us</a>
  </nav>

  <div class="slide abs" role="img" aria-label="Smiling multi-generation family in front of a house with palm trees"></div>
  <div class="slide-arrow prev abs"><svg width="14" height="18" viewBox="0 0 14 18"><path d="M10 2 3 9l7 7" fill="none" stroke="#fff" stroke-width="2.5"/></svg></div>
  <div class="slide-arrow next abs"><svg width="14" height="18" viewBox="0 0 14 18"><path d="M4 2l7 7-7 7" fill="none" stroke="#fff" stroke-width="2.5"/></svg></div>
  <div class="dots abs"><span class="dot"></span><span class="dot active"></span></div>

  <div class="gallery abs" role="img" aria-label="Gallery of modern home interiors and exteriors">
    <div></div><div></div><div></div><div></div><div></div><div></div>
  </div>

  <a class="cta-link abs">CLICK HERE TO GET AN</a>
  <h2 class="cta-title abs heading">INDIVIDUAL HEALTH INSURANCE QUOTE</h2>
  <p class="cta-text abs">Shop Online For An Affordable Individual &amp; Family Health Insurance Plan. All Major Companies Represented.</p>

  <div class="stats abs">
    <div class="stat"><div class="stat-label">Built Year</div><div class="stat-value">2017</div></div>
    <div class="stat"><div class="stat-label">Clients</div><div class="stat-value">5</div></div>
    <div class="stat"><div class="stat-label">Partners</div><div class="stat-value">3</div></div>
    <div class="stat"><div class="stat-label">Clients</div><div class="stat-value">2</div></div>
    <div class="stat"><div class="stat-label">Clients</div><div class="stat-value">25</div></div>
  </div>
</section>

<section class="about abs">
  <h2 class="about-title abs heading">Who we are?</h2>
  <div class="about-photo abs" role="img" aria-label="Mother holding her baby outside a home"></div>
  <div class="about-text abs">
    <p>Calm Harbor Cover Corporation is an Independent Insurance and Financial Brokerage Firm serving clients throughout Florida and Internationally. We are an experienced team of professionals, committed to our primary mission – to find the less expensive insurance coverage, for protection you want, at the best rate you deserve. Our integrated suite of online services facilitates a comprehensive search and review of leading insurance companies.</p>
    <p><strong>Calm Harbor Cover Corporation</strong> is not owned by any insurance company, therefore we provide objective information to consumers and small business owners, helping them make informed decisions about their insurance and financial needs. We aim to offer you the highest quality insurance and service on the market.</p>
  </div>
</section>

<section class="banner abs" role="img" aria-label="Modern villa with pool and palm trees under a golden tint">
  <h2 class="banner-title abs heading">Lorem ipsum dolor sit amet, consectetur adipiscing elit, sed do eiusmod tempor incididunt ut labore et dolore magna aliqua..</h2>
  <p class="banner-text abs">Lorem ipsum dolor sit amet, consectetur adipiscing elit, sed do eiusmod tempor incididunt ut labore et dolore magna aliqua.</p>
</section>

<footer class="footer abs">
  <div class="agent-photo abs" role="img" aria-label="Portrait of the insurance agent in a suit"></div>
  <h3 class="footer-title abs heading" style="left:464px">About Agent.</h3>
  <p class="footer-text abs" style="left:464px;width:290px">Lorem ipsum dolor sit amet, consectetur adipiscing elit, sed do eiusmod tempor incididunt ut labore et dolore magna aliqua.</p>
  <h3 class="footer-title abs heading" style="left:775px">Our Team</h3>
  <p class="footer-text abs" style="left:775px;width:260px">
    <span class="accent">example@example.com</span><br>
    <span class="accent">(123)-456-789</span><br>
    Example Street,<br>Address Line 2<br>State 101000<br>Country
  </p>
</footer>

</body>
</html>
```